Email Banner (QuillLedger)

We require an email banner for our email promotions sent to prospect clients. The banner needs to contain the wording QuillLedger and use the same colour scheme as the logos attached.

This is for B2B professional's so needs to look like a place you would come to read technology articles.

```html
<!DOCTYPE html>
<html lang="en">
<head>
<meta charset="utf-8">
<title>QuillLedger Email Banners</title>
<link rel="stylesheet" href="https://fonts.googleapis.com/css2?family=Lexend:wght@500&family=Montserrat:wght@700&display=swap">
<style>
  :root {
    --canvas: #e7e7e7;
    --navy: #002042;
    --navy-line: #0d2c52;
    --red: #d3343a;
    --red-faint: #3a1c34;
    --paper: #fbfcfd;
    --paper-pattern: #f1f3f6;
    --rule-light: #e6edf2;
    --rule-dark: #6d7b8a;
    --silver-dark: #8795a4;
    --silver-light: #f6f7f9;
    --mark-grey: #d2d4d6;
    --mark-faint: #33506c;
  }
  * { margin: 0; padding: 0; box-sizing: border-box; }
  html, body { width: 1200px; height: 747px; overflow: hidden; }
  body { background: var(--canvas); position: relative; font-family: "Lexend", sans-serif; }

  .banner { position: absolute; left: 50px; width: 1100px; height: 229px; overflow: hidden; }
  .banner--light { top: 96px; background: var(--paper); }
  .banner--silver { top: 421px; background: var(--navy); }

  .pattern { position: absolute; left: 0; right: 0; }
  .banner--light .pattern { background: var(--paper-pattern); }
  .banner--silver .pattern { background: var(--navy-line); opacity: .55; }

  .band { position: absolute; }
  .band::before, .band::after {
    content: ""; position: absolute; left: 0; right: 0; height: 3px;
  }
  .band::before { top: 0; }
  .band::after { bottom: 0; }

  .banner--light .band {
    left: 0; right: 0; top: 47px; height: 133px; background: var(--paper);
  }
  .banner--light .band::before, .banner--light .band::after {
    background: linear-gradient(90deg, var(--rule-light) 20%, var(--rule-dark) 55%, var(--rule-light) 85%);
  }

  .banner--silver .band {
    left: 0; width: 790px; top: 46px; height: 135px;
    background: linear-gradient(90deg, var(--silver-dark) 0%, #d2d7dc 35%, var(--silver-light) 50%, #b5bec7 75%, var(--silver-dark) 100%);
  }
  .banner--silver .band::before, .banner--silver .band::after {
    background: linear-gradient(90deg, #b8c2cc, #e8edf0 50%, #b8c2cc);
  }

  .side { position: absolute; top: 0; bottom: 0; background: var(--navy); }
  .banner--light .side { left: 0; width: 380px; }
  .banner--silver .side { left: 790px; right: 0; }

  .edge { position: absolute; top: 0; height: 229px; width: 40px; }
  .banner--light .edge { left: 372px; }
  .banner--silver .edge { left: 774px; }

  .wordmark {
    position: absolute; z-index: 2; white-space: nowrap;
    color: var(--navy); font-weight: 500; letter-spacing: .5px; line-height: 1;
  }
  .banner--light .wordmark { left: 540px; top: 90px; font-size: 54px; }

  .wordmark-line { position: absolute; right: 610px; font-size: 50px; white-space: nowrap;
    color: var(--navy); font-weight: 500; letter-spacing: .5px; line-height: 1; z-index: 2; }
  .wordmark-line--top { top: 65px; }
  .wordmark-line--bottom { top: 100px; }

  .accent { position: absolute; background: var(--red); z-index: 2; }
  .banner--light .accent--main { left: 918px; top: 114px; width: 13px; height: 13px; }
  .banner--silver .accent--main { left: 292px; top: 117px; width: 14px; height: 14px; }

  .side-name { position: absolute; white-space: nowrap; font-weight: 500; line-height: 1; }
  .banner--light .side-name { left: 90px; top: 97px; font-size: 34px; color: var(--mark-grey); }
  .banner--silver .side-name { left: 70px; top: 102px; font-size: 36px; color: var(--mark-faint); }

  .accent--side-light { left: 296px; top: 112px; width: 12px; height: 12px; }
  .accent--side-dark { left: 290px; top: 117px; width: 13px; height: 13px; background: var(--red-faint); }

  .cta {
    position: absolute; top: 0; right: 0; width: 119px; height: 26px;
    border-bottom-left-radius: 11px;
    font-family: "Montserrat", sans-serif; font-weight: 700; font-size: 14.5px;
    display: flex; align-items: center; justify-content: center; letter-spacing: .3px;
    text-decoration: none; z-index: 3;
  }
  .banner--light .cta { background: var(--navy); color: #fff; }
  .banner--silver .cta { background: #fff; color: var(--navy); }
</style>
</head>
<body>

<section class="banner banner--light">
  <div class="pattern" style="top:0;height:47px" role="img" aria-label="Light geometric hexagon pattern"></div>
  <div class="pattern" style="bottom:0;height:49px" role="img" aria-label="Light geometric hexagon pattern"></div>
  <div class="band"></div>
  <span class="wordmark">QuillLedger</span>
  <span class="accent accent--main"></span>
  <div class="side">
    <span class="side-name">QuillLedger</span>
    <span class="accent accent--side-light"></span>
  </div>
  <svg class="edge" viewBox="0 0 40 229" aria-hidden="true">
    <g fill="#002042" stroke="#e3ecf3" stroke-width="3">
      <rect x="-20" y="0" width="50" height="12" rx="6"/>
      <rect x="-20" y="16" width="42" height="12" rx="6"/>
      <rect x="-20" y="47" width="44" height="12" rx="6"/>
      <rect x="-20" y="62" width="52" height="14" rx="7"/>
      <rect x="-20" y="78" width="50" height="14" rx="7"/>
      <rect x="-20" y="109" width="44" height="12" rx="6"/>
      <rect x="-20" y="124" width="42" height="12" rx="6"/>
      <rect x="-20" y="139" width="50" height="14" rx="7"/>
      <rect x="-20" y="155" width="52" height="14" rx="7"/>
      <rect x="-20" y="171" width="42" height="12" rx="6"/>
      <rect x="-20" y="202" width="44" height="12" rx="6"/>
      <rect x="-20" y="217" width="50" height="12" rx="6"/>
    </g>
    <rect x="0" y="0" width="14" height="229" fill="#002042"/>
  </svg>
  <a class="cta" href="#">CLICK HERE</a>
</section>

<section class="banner banner--silver">
  <div class="pattern" style="top:0;height:46px" role="img" aria-label="Dark geometric hexagon pattern"></div>
  <div class="pattern" style="bottom:0;height:48px" role="img" aria-label="Dark geometric hexagon pattern"></div>
  <div class="band"></div>
  <span class="wordmark-line wordmark-line--top">Quill</span>
  <span class="wordmark-line wordmark-line--bottom">Ledger</span>
  <span class="accent accent--main"></span>
  <div class="side">
    <span class="side-name">QuillLedger</span>
    <span class="accent accent--side-dark"></span>
  </div>
  <svg class="edge" viewBox="0 0 40 229" aria-hidden="true">
    <rect x="16" y="0" width="24" height="229" fill="#002042"/>
    <g fill="#002042" stroke="#ffffff" stroke-width="3">
      <rect x="4" y="0" width="40" height="14" rx="7"/>
      <rect x="10" y="16" width="36" height="14" rx="7"/>
      <rect x="12" y="46" width="34" height="14" rx="7"/>
      <rect x="4" y="62" width="40" height="14" rx="7"/>
      <rect x="8" y="78" width="38" height="14" rx="7"/>
      <rect x="12" y="108" width="34" height="14" rx="7"/>
      <rect x="4" y="124" width="40" height="14" rx="7"/>
      <rect x="8" y="140" width="38" height="14" rx="7"/>
      <rect x="12" y="170" width="34" height="14" rx="7"/>
      <rect x="8" y="186" width="38" height="14" rx="7"/>
      <rect x="4" y="202" width="40" height="14" rx="7"/>
      <rect x="8" y="218" width="38" height="14" rx="7"/>
    </g>
    <rect x="22" y="0" width="18" height="229" fill="#002042"/>
  </svg>
  <a class="cta" href="#">CLICK HERE</a>
</section>

</body>
</html>
```